Business Card Design Project

Build kick ass business card.
Updates

I just uploaded the Veruxo Logo in AI format, for those that were asking. It's looking real good and we'll be reviewing the designs soon. Thanks. 

Target Market(s)

Businesses in many verticals. Focusing on information security.

Veruxo, LLC
Darren Colby
Principal Security Consultant
Mobile: +1-480-555-0137
Email: Darren.Colby@Veruxo.example
Web: www.veruxo.example

Industry/Entity Type

Business

Requirements
Must have
• Design must look high-end, hi-tech stylish and minimalist

Be different – one that stands out from thousands of others

Does not have to be traditional rectangle

Would like logo integrated

```html
<!DOCTYPE html>
<html lang="en">
<head>
<meta charset="utf-8">
<title>Veruxo Business Card</title>
<link rel="stylesheet" href="https://fonts.googleapis.com/css2?family=Open+Sans:ital,wght@0,400;0,600;1,700&family=Libre+Baskerville&display=swap">
<style>
  :root {
    --page-bg: #d9d9db;
    --card-white: #ffffff;
    --card-black: #050505;
    --ink-dark: #2f2f31;
    --ink-mid: #3a3a3c;
    --label-ink: #444446;
    --accent-blue: #1d8ccf;
    --card-edge: #b9b9bc;
  }
  * { margin: 0; padding: 0; box-sizing: border-box; }
  html, body { width: 1200px; height: 765px; overflow: hidden; }
  body {
    background: var(--page-bg);
    font-family: "Open Sans", Arial, sans-serif;
    position: relative;
  }
  .card {
    position: absolute;
    top: 301px;
    width: 575px;
    height: 345px;
    border-radius: 36px;
    overflow: hidden;
  }
  .card--front { left: 16px; background: var(--card-black); }
  .card--back { left: 604px; background: var(--card-white); border: 1px solid var(--card-edge); }

  .front-imagery {
    position: absolute; inset: 0;
    background: linear-gradient(135deg, #0a0a0a 0%, #2b2b2b 30%, #050505 50%, #3c3c3c 72%, #0b0b0b 100%);
  }
  .brand-band {
    position: absolute;
    left: 0; top: 93px;
    width: 325px; height: 105px;
    background: var(--card-white);
    display: flex; align-items: center;
    padding-left: 42px; gap: 16px;
  }
  .brand-mark { width: 44px; height: 44px; flex: none; }
  .brand-name {
    font-size: 38px; font-weight: 400; letter-spacing: 1px;
    color: var(--ink-dark);
  }

  .back-imagery {
    position: absolute; inset: 0;
    background: linear-gradient(125deg, #ffffff 0%, #f1f1f2 35%, #fbfbfb 55%, #ececed 80%, #ffffff 100%);
  }
  .holder {
    position: absolute; left: 38px; top: 110px;
    display: flex; align-items: flex-start; gap: 8px;
  }
  .holder-name {
    font-size: 39px; font-weight: 600; letter-spacing: -1.2px;
    color: var(--ink-dark); line-height: 1;
  }
  .holder-role {
    font-size: 14.5px; line-height: 17px; color: var(--ink-mid);
    padding-top: 2px;
  }
  .contact-list {
    position: absolute; left: 43px; top: 187px;
    list-style: none; font-size: 15px; line-height: 21px;
    color: var(--ink-mid); letter-spacing: 0.3px;
  }
  .contact-list b { font-weight: 700; font-style: italic; color: var(--ink-dark); }
  .back-brand {
    position: absolute; right: 44px; bottom: 50px;
    display: flex; align-items: center; gap: 8px;
  }
  .back-brand .brand-mark { width: 18px; height: 18px; }
  .back-brand .brand-name { font-size: 19px; letter-spacing: 0.5px; }

  .side-label {
    position: absolute; top: 686px;
    font-family: "Libre Baskerville", Georgia, serif;
    font-size: 14px; letter-spacing: 3px; color: var(--label-ink);
  }
  .side-label--front { left: 66px; }
  .side-label--back { left: 660px; }
</style>
</head>
<body>
  <section class="card card--front">
    <div class="front-imagery" role="img" aria-label="Dark glossy black-and-chrome abstract technology surface"></div>
    <div class="brand-band">
      <svg class="brand-mark" viewBox="0 0 44 44" aria-hidden="true"><circle cx="22" cy="22" r="20" fill="var(--accent-blue)"/></svg>
      <span class="brand-name">VERUXO</span>
    </div>
  </section>

  <section class="card card--back">
    <div class="back-imagery" role="img" aria-label="Faint pale grey abstract technology surface"></div>
    <div class="holder">
      <h1 class="holder-name">Darren Colby</h1>
      <p class="holder-role">Veruxo, LLC<br>Principal Security Consultant</p>
    </div>
    <ul class="contact-list">
      <li>Mobile: <b>+1-480-555-0137</b></li>
      <li>Email: <b>Darren.Colby@Veruxo.example</b></li>
      <li>Web: <b>www.veruxo.example</b></li>
    </ul>
    <div class="back-brand">
      <svg class="brand-mark" viewBox="0 0 18 18" aria-hidden="true"><circle cx="9" cy="9" r="8" fill="var(--accent-blue)"/></svg>
      <span class="brand-name">VERUXO</span>
    </div>
  </section>

  <p class="side-label side-label--front">FRONT</p>
  <p class="side-label side-label--back">BACK</p>
</body>
</html>
```